Business Card Design

We are looking for a double sided business card.

On one side would be our logo

On the Other Side

Martin Kolby
Sales and Marketing

Phone/Text Logo and 530-418-2763
Email Logo and info@plumvalepets.com
Website Logo and www.plumvalepets.com
Facebook Logo and plumvale pets
Instagram Logo and plumvale_pets

Target Market(s)

Pet owners

Contact Information for Business Card

In project description

Requirements
Must have
• Logo

```html
<!DOCTYPE html>
<html lang="en">
<head>
<meta charset="utf-8">
<title>Plumvale Pets – Business Card</title>
<link href="https://fonts.googleapis.com/css2?family=Montserrat:wght@400;500;700&display=swap" rel="stylesheet">
<style>
  :root {
    --backdrop: #c8c8c8;
    --card: #121212;
    --card-edge: #0a0a0a;
    --orange: #f5a31a;
    --white: #f2f2f2;
    --pattern-light: #5a5a5a;
    --pattern-dark: #0d0d0d;
  }
  * { margin: 0; padding: 0; box-sizing: border-box; }
  html, body {
    width: 1200px; height: 900px; overflow: hidden;
    background: var(--backdrop);
    font-family: "Montserrat", sans-serif;
  }
  .sheet {
    position: relative; width: 1200px; height: 900px;
    display: flex; flex-direction: column; align-items: center; justify-content: center; gap: 30px;
  }
  .card {
    position: relative; width: 700px; height: 400px;
    background: var(--card);
    box-shadow: 0 10px 24px rgba(0,0,0,.35);
    overflow: hidden;
  }
  /* Logo side */
  .card--brand .pattern-fill {
    position: absolute; inset: 0;
    background: linear-gradient(150deg, var(--pattern-light) 0%, #2a2a2a 30%, var(--pattern-dark) 65%, #1a1a1a 100%);
  }
  .card--brand .brand-name {
    position: absolute; left: 50%; top: 50%; transform: translate(-50%, -50%);
    font-weight: 700; font-size: 40px; letter-spacing: 1px;
    color: var(--white); background: var(--card); padding: 14px 26px; white-space: nowrap;
  }
  /* Contact side */
  .card--contact .brand-block {
    position: absolute; left: 40px; top: 0; bottom: 0; width: 270px;
    display: flex; align-items: center; justify-content: center;
  }
  .card--contact .brand-block .brand-name {
    font-weight: 700; font-size: 34px; line-height: 1.1; color: var(--white); text-align: center;
  }
  .divider {
    position: absolute; left: 335px; top: 110px; height: 190px; width: 2px; background: var(--orange);
  }
  .details { position: absolute; left: 362px; top: 104px; color: var(--white); }
  .person-name { font-weight: 700; font-size: 30px; color: var(--orange); line-height: 1.1; }
  .person-role { font-weight: 400; font-size: 17px; margin-top: 4px; margin-bottom: 14px; }
  .contact-list { list-style: none; }
  .contact-list li {
    display: flex; align-items: center; gap: 12px;
    font-size: 18px; line-height: 1; margin-bottom: 11px;
  }
  .contact-list svg { width: 18px; height: 18px; flex: none; }
</style>
</head>
<body>
<main class="sheet">

  <section class="card card--brand" aria-label="Card logo side">
    <div class="pattern-fill" role="img" aria-label="Repeating brand monogram pattern in glossy black and silver"></div>
    <div class="brand-name">Plumvale Pets</div>
  </section>

  <section class="card card--contact" aria-label="Card contact side">
    <div class="brand-block">
      <div class="brand-name">Plumvale<br>Pets</div>
    </div>
    <div class="divider"></div>
    <div class="details">
      <h1 class="person-name">Martin Kolby</h1>
      <p class="person-role">Sales and Marketing</p>
      <ul class="contact-list">
        <li>
          <svg viewBox="0 0 24 24" aria-hidden="true"><path fill="var(--orange)" d="M6.6 10.8a15.1 15.1 0 0 0 6.6 6.6l2.2-2.2a1 1 0 0 1 1-.25 11.4 11.4 0 0 0 3.6.57 1 1 0 0 1 1 1V20a1 1 0 0 1-1 1A17 17 0 0 1 3 4a1 1 0 0 1 1-1h3.5a1 1 0 0 1 1 1c0 1.25.2 2.45.57 3.6a1 1 0 0 1-.25 1z"/></svg>
          530-418-2763
        </li>
        <li>
          <svg viewBox="0 0 24 24" aria-hidden="true"><rect x="2" y="5" width="20" height="14" rx="1.5" fill="var(--orange)"/><path d="M3 6l9 7 9-7" fill="none" stroke="var(--card)" stroke-width="1.8"/></svg>
          info@plumvalepets.com
        </li>
        <li>
          <svg viewBox="0 0 24 24" aria-hidden="true"><circle cx="12" cy="12" r="9.5" fill="none" stroke="var(--orange)" stroke-width="2"/><ellipse cx="12" cy="12" rx="4" ry="9.5" fill="none" stroke="var(--orange)" stroke-width="1.6"/><path d="M2.5 12h19" stroke="var(--orange)" stroke-width="1.6"/></svg>
          www.plumvalepets.com
        </li>
        <li>
          <svg viewBox="0 0 24 24" aria-hidden="true"><circle cx="12" cy="12" r="10" fill="var(--orange)"/></svg>
          plumvale pets
        </li>
        <li>
          <svg viewBox="0 0 24 24" aria-hidden="true"><circle cx="12" cy="12" r="10" fill="var(--orange)"/></svg>
          plumvale pets
        </li>
      </ul>
    </div>
  </section>

</main>
</body>
</html>
```